VOLQ Marketing Sell Sheets Design

I need a flyer that I can use to market and advertise my business utilizing the logo that you already created. I will attach in detail a copy of the design specifics for the layout of the flyer as well as the content of each flyer. The color scheme will be the same as the logo you designed. Blues, greys, blacks, White

Target Market(s)

Insurance

Industry/Entity Type

Insurance Blue

Font styles to use
Sans Serif

Colors
3176b5
cfdeed
eaf1f7

Requirements
Must have
• I need 6 individual sheets on 8.5 X 11. The layout will be as per the layout I have marked up and described in the brief. The only change on each flyer is the content which I have submitted 6 descriptions along with content. The logo and color scheme will be as described In the brief.
Nice to have
• No preference
Should not have
• No preference

```html
<!DOCTYPE html>
<html lang="en">
<head>
<meta charset="utf-8">
<title>VOLQ Marketing Sell Sheets</title>
<link rel="stylesheet" href="https://fonts.googleapis.com/css2?family=Oswald:wght@500;700&family=Roboto:wght@300;400;500&family=Roboto+Condensed:ital,wght@1,500&family=Cormorant+SC:wght@500;600&family=Montserrat:wght@700&display=swap">
<style>
:root{
  --navy:#2c3f90;
  --navy-deep:#23347a;
  --blue:#3176b5;
  --blue-pale:#cfdeed;
  --blue-mist:#eaf1f7;
  --grey-bg:#d9d9db;
  --grey-band-l:#a9a9ab;
  --grey-band-d:#505052;
  --ink:#333;
  --white:#fff;
}
*{margin:0;padding:0;box-sizing:border-box}
html,body{width:1200px;height:890px;overflow:hidden}
body{background:var(--grey-bg);position:relative;font-family:"Roboto",sans-serif;color:var(--ink)}

.sheet{position:absolute;top:79px;width:542px;height:701px;overflow:hidden;box-shadow:0 2px 8px rgba(0,0,0,.25)}
.sheet--front{left:48px;background:var(--white)}
.sheet--back{left:614px;background:var(--white)}

/* FRONT */
.front__topbar{position:absolute;left:0;top:0;width:100%;height:19px;background:var(--navy)}
.front__intro{position:absolute;left:0;top:19px;width:222px;height:433px;background:linear-gradient(90deg,#f4f4f5,#fff 40%,#e4e4e6)}
.brand{position:absolute;left:16px;top:48px;display:flex;align-items:center;gap:8px}
.brand__square{width:30px;height:30px;background:var(--navy)}
.brand__name{font-family:"Cormorant SC",serif;font-weight:600;font-size:19px;color:var(--navy);line-height:1}
.checklist{position:absolute;left:52px;top:110px;list-style:none}
.checklist li{font-family:"Cormorant SC",serif;font-weight:500;font-size:15.5px;color:var(--navy);height:20.4px;display:flex;align-items:center;gap:6px;letter-spacing:.5px}
.checklist svg{width:10px;height:10px}
.front__photo{position:absolute;left:222px;top:19px;width:320px;height:433px;background:linear-gradient(160deg,#1d2f72 0%,#3b5ea8 35%,#7fa2d4 65%,#c8d8ee 100%)}
.value-word{position:absolute;left:236px;font-family:"Oswald",sans-serif;font-weight:700;font-size:50px;line-height:1;color:#d9dce3;text-shadow:2px 2px 3px rgba(0,0,0,.55);letter-spacing:.5px;transform:scaleX(.9);transform-origin:left}
.front__band{position:absolute;left:0;top:452px;width:100%;height:54px;background:linear-gradient(180deg,var(--grey-band-l),var(--grey-band-d));display:flex;align-items:center;padding-left:14px}
.front__band h2{font-family:"Oswald",sans-serif;font-weight:500;font-size:19px;color:#f2f2f2;text-shadow:1px 1px 2px rgba(0,0,0,.6);letter-spacing:.2px}
.front__promise{position:absolute;left:0;top:506px;width:222px;height:159px;background:linear-gradient(90deg,#efeff0,#fff 45%,#e2e2e4);border-right:1px dashed #6a78a8}
.front__promise p{position:absolute;left:57px;top:23px;font-family:"Cormorant SC",serif;font-weight:500;font-size:16px;line-height:20.3px;color:var(--navy);letter-spacing:.4px}
.front__details{position:absolute;left:223px;top:506px;width:319px;height:159px;background:var(--blue-pale);padding:22px 18px 0 14px}
.front__details p{font-size:10px;line-height:13.2px;font-weight:300;color:#333;text-align:justify;margin-bottom:7px}
.contact-bar{position:absolute;left:0;bottom:0;width:100%;height:36px;background:var(--navy);display:flex;align-items:center;padding-left:18px;gap:11px;color:var(--white);font-size:10px;font-weight:300}
.contact-bar span{display:flex;align-items:center;gap:4px;white-space:nowrap}
.contact-bar svg{width:8px;height:8px;fill:var(--white)}

/* BACK */
.back__header{position:absolute;left:0;top:0;width:100%;height:98px;background:var(--navy);text-align:center;color:var(--white)}
.back__title{font-family:"Montserrat",sans-serif;font-weight:700;font-size:34px;line-height:1;padding-top:12px;letter-spacing:.5px}
.back__subtitle{font-weight:300;font-size:21px;line-height:1;margin-top:6px;color:#c7d1ec;letter-spacing:.3px}
.back__tags{display:flex;justify-content:center;margin-top:9px;font-size:9px;font-weight:400;color:#e4e8f4}
.back__tags span{padding:0 11px;border-left:1px solid #9fabd3;line-height:9px}
.back__tags span:first-child{border-left:none}
.back__col{position:absolute;top:98px;height:408px;padding:12px 13px 0 13px}
.back__col--left{left:0;width:271px;background:linear-gradient(90deg,#fafafa,#e6e6e7)}
.back__col--right{left:271px;width:271px;background:var(--blue-pale);padding-left:12px;padding-right:12px}
.service{font-size:6.7px;line-height:8.9px;color:#3a3a3a;text-align:justify;margin-bottom:6px}
.back__col--right .service{margin-bottom:17px}
.service__name{color:var(--navy);font-weight:500}
.service__name--block{display:block}
.back__photo{position:absolute;left:0;top:506px;width:100%;height:131px;background:linear-gradient(180deg,#6b84c4 0%,#3c56a2 45%,#1f2f74 100%)}
.back__question{position:absolute;left:0;top:637px;width:100%;height:64px;background:var(--blue-pale);display:flex;align-items:center;justify-content:center}
.back__question p{font-family:"Roboto Condensed",sans-serif;font-style:italic;font-weight:500;font-size:14.5px;color:var(--navy)}
</style>
</head>
<body>

<section class="sheet sheet--front">
  <div class="front__topbar"></div>
  <div class="front__intro">
    <div class="brand"><span class="brand__square"></span><span class="brand__name">VOLQ Marketing</span></div>
    <ul class="checklist">
      <li><svg viewBox="0 0 10 10"><path d="M1 5.5 L4 8.5 L9 1.5" fill="none" stroke="#2c3f90" stroke-width="1.2"/></svg>Fast</li>
      <li><svg viewBox="0 0 10 10"><path d="M1 5.5 L4 8.5 L9 1.5" fill="none" stroke="#2c3f90" stroke-width="1.2"/></svg>Friendly</li>
      <li><svg viewBox="0 0 10 10"><path d="M1 5.5 L4 8.5 L9 1.5" fill="none" stroke="#2c3f90" stroke-width="1.2"/></svg>Effecient</li>
      <li><svg viewBox="0 0 10 10"><path d="M1 5.5 L4 8.5 L9 1.5" fill="none" stroke="#2c3f90" stroke-width="1.2"/></svg>Secure</li>
    </ul>
  </div>
  <div class="front__photo" role="img" aria-label="Glass office tower seen from below against a blue cloudy sky"></div>
  <span class="value-word" style="top:38px">PROFESSONAL</span>
  <span class="value-word" style="top:144px">RELIABLE</span>
  <span class="value-word" style="top:253px">TRUST</span>
  <span class="value-word" style="top:368px">QUALITY</span>

  <div class="front__band"><h2>LEADERS IN CLAIMS MANAGEMENT</h2></div>
  <div class="front__promise"><p>People you can<br>count on<br>Experience You<br>Can Trust.</p></div>
  <div class="front__details">
    <p>Lorem Ipsum is simply dummy text of the printing and typesetting industry. Lorem Ipsum has been the industry's standard dummy text ever since the 1500s, when an unknown printer took a galley of type and scrambled it to make a type specimen book. It has survived not only five centuries.</p>
    <p>Lorem Ipsum passages, and more recently with desktop publishing software like Pagecraft Studio including versions of Lorem Ipsum.</p>
  </div>
  <div class="contact-bar">
    <span><svg viewBox="0 0 10 10"><path d="M5 0a3.5 3.5 0 0 0-3.5 3.5C1.5 6 5 10 5 10s3.5-4 3.5-6.5A3.5 3.5 0 0 0 5 0zm0 5a1.4 1.4 0 1 1 0-2.8A1.4 1.4 0 0 1 5 5z"/></svg>P.O. Box 5120 Brookfield, TX 75001</span>
    <span><svg viewBox="0 0 10 10"><path d="M2 0l2 2.5-1 1.2c.6 1.3 1.8 2.5 3.2 3.2l1.2-1L10 8l-1.5 2C4 10 0 6 0 1.5z"/></svg>1-800-555-0142</span>
    <span><svg viewBox="0 0 10 10"><path d="M2 0h5v3H2zM0 3.5h10V9H0zm2 2v1h6v-1z"/></svg>555-201-7788</span>
    <span><svg viewBox="0 0 10 10"><path d="M5 0a5 5 0 1 0 0 10A5 5 0 0 0 5 0zm0 1c.6.7 1 1.8 1.1 3.5H3.9C4 2.8 4.4 1.7 5 1zM1 5.5h2c0 1.4.3 2.5.8 3.3A4 4 0 0 1 1 5.5zm2-1H1A4 4 0 0 1 3.8 1.2C3.3 2 3 3.1 3 4.5zm2 4.5c-.6-.7-1-1.8-1.1-3.5h2.2C6 7.2 5.6 8.3 5 9zm1.2-.2c.5-.8.8-1.9.8-3.3h2a4 4 0 0 1-2.8 3.3zM7 4.5c0-1.4-.3-2.5-.8-3.3A4 4 0 0 1 9 4.5z"/></svg>volqmarketing.example</span>
  </div>
</section>

<section class="sheet sheet--back">
  <header class="back__header">
    <h1 class="back__title">EHS MANAGEMENT</h1>
    <p class="back__subtitle">LEADERS IN CLAIMS MANAGEMENT</p>
    <div class="back__tags"><span>PROFESSIONAL</span><span>RELIABLE</span><span>TRUST</span><span>QUALITY</span></div>
  </header>

  <div class="back__col back__col--left">
    <p class="service"><span class="service__name">EHS Programs VOLQ Marketing</span> staff bring the technical skill and regulatory knowledge needed to design strong programs that identify, review and control workplace safety and health hazards. Our team of scientists and engineers has spent many years designing and running programs that cut illness and accidents across many sites. In addition, VOLQ Marketing offers training and compliance audit services that help clients plan budgets and set priorities for the steps needed to keep every safety program on track and fully in line with current regulations and program goals.</p>
    <p class="service"><span class="service__name service__name--block">Waste Management, Treatment &amp; Disposal</span>VOLQ Marketing staff has broad experience on hundreds of projects covering the handling, treatment and disposal of a wide range of waste types and blends from city, industrial, commercial and public sources, including many hospitals and schools. Such projects have covered city solid waste, medical and lab waste, hazardous and chemical waste, and other special waste. Many projects have also dealt with recycling and reuse, resource and material recovery, incineration, and newer treatment methods such as waste-to-energy systems.</p>
    <p class="service"><span class="service__name service__name--block">Water, Wastewater &amp; Storm water Management Def.</span>VOLQ Marketing provides a wide set of planning and study services covering water quality, storm water and wastewater control, pollution prevention and environmental permits. Our staff has deep experience in shaping and carrying out fixes for existing and likely water problems at client sites.</p>
    <p class="service"><span class="service__name">Emergency Response</span> Based on thirty years of experience providing emergency response services to both the insurance and energy industries, VOLQ Marketing has found that a quick reply is vital to controlling incidents, building good ties with regulators, cutting harm to property and health, and keeping response and cleanup costs down. Through our own emergency response team, VOLQ Marketing offers help around the clock, seven days a week, to deal with sudden events and to limit their possible impact on people and sites.</p>
    <p class="service"><span class="service__name">Site Investigation</span> VOLQ Marketing offers many kinds of site study services, including subsurface checks, cause and origin reviews, forensic and transport studies, and indoor air quality tests. Most studies focus on measuring the extent and size of any damage. They also support decisions on risk review and site cleanup. Our team draws on long experience in risk control and site repair to build focused study plans that give clear facts and help clients choose cost-effective paths toward timely site closure with the agencies involved.</p>
  </div>

  <div class="back__col back__col--right">
    <p class="service"><span class="service__name service__name--block">Air Pollution Control &amp; Air Quality Management</span>VOLQ Marketing staff has broad, detailed experience in the engineering, design, building and running of air control systems and equipment, covering a wide range of combustion and emission sources such as boilers, backup generators, industrial furnaces and incinerators. Our skills include permits under federal and state rules, yearly emission counts, source checks and reports, compliance test support, and air quality impact studies.</p>
    <p class="service"><span class="service__name service__name--block">Environmental Site Assessment Def. 7</span>VOLQ Marketing performs complete, well priced site assessments for lenders, developers, lawyers, insurers and private clients. Each assessment is carried out to client needs or in line with current industry standards for first-phase reviews and transaction screens, with clear findings and next steps.</p>
    <p class="service"><span class="service__name service__name--block">Soil/Groundwater Remediation</span>VOLQ Marketing can serve as lead contractor for site study, cleanup design, repair work and project control, or as a technical guide that makes sure resources are used well and waste is kept low. We have designed, built and run hundreds of cleanup systems to recover, hold or remove fuel, other chemical and metal releases in every stage of the process.</p>
    <p class="service"><span class="service__name service__name--block">Regulatory Support, Permitting &amp; Compliance</span>VOLQ Marketing reviews new and proposed rules so that our team keeps up to date on compliance and environmental issues. We study and explain complex regulations for our commercial and industrial clients so that they meet every permit and compliance need. VOLQ Marketing also has wide experience working with federal regulators and many state agencies.</p>
  </div>

  <div class="back__photo" role="img" aria-label="Business people in silhouette in a glass office lobby overlooking a city skyline, tinted blue"></div>
  <div class="back__question"><p>How can VOLQ Marketing help you recover from the unexpected?</p></div>
</section>

</body>
</html>
```